Need new label for my eczema cream. Marinelle Daily Relief. PLS NOTHING LAME AND CLIP ART-ISH!

Think corvanta website meets eczema....our site is pinegrovesoothe.com ill attach our current logo.

```html
<!DOCTYPE html>
<html lang="en">
<head>
<meta charset="UTF-8">
<title>Marinelle Daily Relief – Soothing Cream Label</title>
<link href="https://fonts.googleapis.com/css2?family=Montserrat:wght@600;700;800&family=Poppins:wght@300;400;500;600;700&display=swap" rel="stylesheet">
<style>
  :root {
    --backdrop: #d9d9d9;
    --label: #ffffff;
    --navy: #1f1b6e;
    --sky: #5fc6ee;
    --sand-light: #f6e6d3;
    --sand: #efd9bf;
  }
  * { margin: 0; padding: 0; box-sizing: border-box; }
  html, body { width: 1074px; height: 1200px; overflow: hidden; }
  body {
    background: var(--backdrop);
    font-family: "Poppins", sans-serif;
    color: var(--navy);
    position: relative;
  }
  .label {
    position: absolute;
    left: 44px; top: 857px;
    width: 990px; height: 213px;
    background: var(--label);
    overflow: hidden;
  }
  .label { top: 492px; left: 32px; width: 1010px; height: 217px; }
  .wave-field {
    position: absolute; left: 0; top: 0;
    width: 100%; height: 100%;
  }
  .panel { position: absolute; }

  /* usage panel */
  .panel-usage { left: 17px; top: 10px; width: 240px; }
  .heading {
    font-family: "Montserrat", sans-serif;
    font-weight: 800; font-size: 11.5px; letter-spacing: 1.2px;
  }
  .usage-text { font-size: 10px; line-height: 12px; margin-top: 3px; font-weight: 400; }
  .external { font-weight: 700; font-size: 8.5px; margin-top: 8px; letter-spacing: .3px; }
  .disclaimer { font-size: 7px; line-height: 9px; margin-top: 3px; font-weight: 300; }
  .heading.ingredients { margin-top: 6px; letter-spacing: 1.8px; }
  .ingredient-list {
    font-size: 6.5px; line-height: 9.1px; font-weight: 600;
    text-align: justify; margin-top: 1px;
  }

  /* brand panel */
  .panel-brand { left: 380px; top: 18px; width: 300px; }
  .category { font-size: 11px; letter-spacing: 6.3px; font-weight: 400; }
  .product-name {
    font-family: "Montserrat", sans-serif;
    font-weight: 800; font-size: 22.5px; line-height: 29px;
    letter-spacing: 2.4px; margin-top: 13px;
  }
  .key-ingredients {
    font-family: "Montserrat", sans-serif;
    font-weight: 700; font-size: 15px; letter-spacing: 2.1px;
    color: var(--sky); margin-top: 4px;
  }
  .volume { position: absolute; left: 380px; top: 191px; font-size: 9.5px; font-weight: 600; }

  /* claims panel */
  .panel-claims { right: 18px; top: 12px; width: 320px; text-align: right; }
  .claim {
    font-family: "Montserrat", sans-serif;
    font-weight: 800; font-size: 13px; letter-spacing: 1.9px; line-height: 22.5px;
  }
  .social { font-size: 9px; font-weight: 600; letter-spacing: .6px; margin-top: 9px; }
  .origin { font-size: 5.5px; font-weight: 600; margin-top: 4px; }
  .distributor {
    font-size: 6px; font-weight: 600; letter-spacing: 1.4px; line-height: 9.5px; margin-top: 4px;
  }
  .product-line {
    position: absolute; right: 18px; top: 196px;
    font-size: 6.8px; font-weight: 600;
  }
</style>
</head>
<body>
  <div class="label">
    <svg class="wave-field" viewBox="0 0 1010 217" preserveAspectRatio="none" role="img" aria-label="Fine-line ocean wave pattern in soft sand tones across the lower label">
      <defs>
        <linearGradient id="sand-fade" x1="0" y1="0" x2="0" y2="1">
          <stop offset="0" stop-color="var(--sand-light)"/>
          <stop offset="1" stop-color="var(--sand)"/>
        </linearGradient>
      </defs>
      <path d="M0 112 C120 100 240 150 330 130 C400 115 450 120 500 105 C560 125 620 150 700 140 C820 125 900 95 1010 105 L1010 217 L0 217 Z" fill="url(#sand-fade)" opacity=".55"/>
    </svg>

    <section class="panel panel-usage">
      <h2 class="heading">HOW TO USE</h2>
      <p class="usage-text">Apply a small amount onto the skin's desired<br>area 1-3 times per day.</p>
      <p class="external">For external use only.</p>
      <p class="disclaimer">May help the appearance of dry, red, flaky skin.<br>This product is not designed to treat or cure eczema.</p>
      <h2 class="heading ingredients">INGREDIENTS</h2>
      <p class="ingredient-list">Aloe Barbadensis (Aloe Vera) Leaf Juice Organic, Helianthus Annuus (Sunflower) Seed Oil Organic, Emulsifying Wax NF, Stearic Acid, Vegetable Glycerin, Caprylic/Capric Triglyceride (Fractionated Coconut Oil), Butyrospermum Parkii (Shea Nut Butter) Organic, Avena Sativa (Colloidal Oatmeal) Kernel Flour, Simmondsia Chinensis (Jojoba) Seed Oil Organic, Polyacrylamide, C13-14 Isoparaffin, Laureth-7, Phenoxyethanol, Ethylhexylglycerin, Chondrus Crispus (Irish Moss) Extract, Oenothera Biennis (Evening Primrose) Oil Organic, Tocopherol (Vitamin E), Sodium Hyaluronate (Hyaluronic Acid), Linoleic Acid, Schinziophyton Rautanenii (Mongongo) Kernal Oil Virgin Organic, Bisabolol With US and imported materials.</p>
    </section>

    <section class="panel panel-brand">
      <p class="category">SOOTHING CREAM</p>
      <h1 class="product-name">MARINELLE<br>DAILY RELIEF</h1>
      <p class="key-ingredients">Sea Moss | Aloe Vera | Oats</p>
    </section>
    <p class="volume">4 fl oz / 118 mL</p>

    <section class="panel panel-claims">
      <p class="claim">FOR ECZEMA-PRONE SKIN</p>
      <p class="claim">NATURAL FROM THE SEA</p>
      <p class="claim">OCEANIC MINERALS</p>
      <p class="social">FOLLOW US @pinegrovesoothe</p>
      <p class="origin">Made in the USA*</p>
      <p class="distributor">DISTRIBUTED BY<br>PINE GROVE SOOTHE LLC<br>CORAL BAY SPRINGS FL, 33100</p>
    </section>
    <p class="product-line">NEW Marinelle Daily Relief Cream 4 fl oz / 118 mL</p>
  </div>
</body>
</html>
```